Solar Energy Technology Company - Solar Savings Analysis Flyer

I Have Included The Text Content I Want Put On An 8 1/2 " x 11" Flyer.

I Want To See It In One Page Format And In Tri-Fold Brochure Format.

It Needs To Grab And Captivate Prospective Customers, Awesome Graphics, Layout, Etc.

We Are A Cutting Edge Solar Energy Solutions & Technology Company.

We Need A World Class High Tech Look and Logo For Our Company Included On Our 8 1/2 x 11 Flyer & Trifold Brochure

Vantora Field Works, LLC
"Bright Horizon Forward"

Would Like A Black Gold And Electric Blue Color Scheme, However, We We Are Open To Seeing Your Creativity, Colors, Graphics Etc. For Consideration.

Target Market(s)

Homeowners Without Solar Panels On Their Roof

Industry/Entity Type

New Roof Top Solar Energy Producing Panel Technology Systems

Font styles to use
Serif

Requirements
Must have
• See My Attached Flyer/Trifold Brochure Display Content
Nice to have
• Gold Black And Electric Blue Color Scheme, Solar Theme Background Graphics

```html
<!DOCTYPE html>
<html lang="en">
<head>
<meta charset="utf-8">
<title>Sunvale Benefits – Solar Savings Flyer</title>
<link rel="stylesheet" href="https://fonts.googleapis.com/css2?family=Rubik:wght@400;500;700;800&family=Oswald:wght@500;600&display=swap">
<style>
  :root{
    --page:#7a7a7a;
    --paper:#ffffff;
    --sky:#4b63c0;
    --night:#1a1a33;
    --gold:#f39a1b;
    --orange:#e8692b;
    --ink:#111111;
    --text:#2b2b2b;
    --peach:#fdeee4;
  }
  *{box-sizing:border-box;margin:0;padding:0}
  html,body{width:1200px;height:1200px;overflow:hidden}
  body{background:var(--page);font-family:"Rubik",sans-serif;color:var(--text);position:relative}
  .flyer{position:absolute;left:187px;top:20px;width:826px;height:1160px;background:var(--paper);overflow:hidden;
    box-shadow:0 6px 18px rgba(0,0,0,.25)}
  .hero-photo{position:absolute;left:0;top:0;width:826px;height:560px;
    background:linear-gradient(180deg,var(--sky) 0%,#3c4c98 18%,#232647 45%,#2a2430 70%,#6b4a2a 82%,rgba(255,255,255,0) 100%)}
  .hero-glow{position:absolute;left:460px;top:300px;width:340px;height:200px;
    background:radial-gradient(ellipse at center,rgba(240,170,70,.45),rgba(240,170,70,0) 70%)}
  .badge{position:absolute;right:0;top:0;width:182px;height:90px;background:var(--gold);border-bottom-left-radius:20px;
    color:#fff;font-weight:700;font-size:19px;line-height:20px;text-align:center;padding-top:24px}
  .brand{position:absolute;left:63px;top:38px;display:flex;align-items:center;gap:10px;color:#fff;font-weight:500;font-size:30px;letter-spacing:-.5px}
  .brand-square{width:18px;height:18px;background:var(--gold)}
  .headline{position:absolute;left:63px;top:105px;font-weight:800;font-size:49px;line-height:53px;text-shadow:0 2px 4px rgba(0,0,0,.6)}
  .headline .l1{color:var(--gold)}
  .headline .l2,.headline .l3{color:var(--orange)}
  .hook{position:absolute;left:66px;color:#fff}
  .hook.q{top:283px;font-size:16px}
  .hook.pay{top:304px;font-size:31px;font-weight:800;color:var(--gold);text-shadow:0 2px 3px rgba(0,0,0,.6)}
  .hook.when{top:358px;font-size:16px}
  .pill{position:absolute;left:64px;background:var(--orange);color:#fff;font-weight:700;border-radius:5px;padding:0 5px}
  .pill.lower{top:380px;font-size:15px;line-height:20px}
  .hook.bill{top:403px;font-size:16px}
  .pill.pct{top:424px;font-size:30px;line-height:34px;background:var(--gold);font-weight:800}
  .intro{position:absolute;left:56px;top:521px;width:716px;font-size:14.5px;line-height:20px;text-align:justify;letter-spacing:.2px}
  .intro b{color:var(--ink);font-size:16px}
  .rates{position:absolute;left:56px;top:597px;width:716px;border:2px solid var(--orange);border-collapse:collapse}
  .rates th{background:var(--orange);color:#fff;text-align:left;font-weight:700;font-size:17px;height:34px;padding-left:12px}
  .rates td{border-top:2px solid var(--orange);height:38px;padding-left:12px;font-weight:700;font-size:18px;color:var(--ink);
    background:linear-gradient(90deg,#fff 40%,var(--peach))}
  .rates small{font-weight:400;font-size:13px}
  .offer{position:absolute;left:56px;top:851px;width:716px;font-size:14.5px;line-height:20px;text-align:justify;letter-spacing:.3px}
  .offer b{color:var(--ink)}
  .url{position:absolute;left:56px;top:943px;width:712px;height:45px;background:var(--ink);border-radius:6px;color:#fff;
    font-weight:700;font-size:27px;letter-spacing:7.5px;text-align:center;line-height:45px}
  .cta{position:absolute;left:56px;top:994px;font-family:"Oswald",sans-serif;font-weight:600;font-size:20px;color:var(--ink);letter-spacing:-.3px}
  .cta span{color:var(--orange)}
  .contact{position:absolute;left:48px;top:1046px;width:300px;white-space:nowrap}
  .phone{font-weight:700;font-size:23px;line-height:30px;color:var(--ink)}
  .rep{font-weight:800;font-size:40px;line-height:46px;color:var(--orange);letter-spacing:-.5px}
  .divider{position:absolute;left:360px;top:1052px;width:2px;height:72px;background:var(--orange)}
  .company{position:absolute;left:378px;top:1050px;font-size:15px;line-height:23px;color:var(--ink);font-family:"Oswald",sans-serif;font-weight:500;white-space:nowrap}
  .company .name{font-family:"Rubik",sans-serif;font-weight:700;font-size:19px;color:var(--orange);letter-spacing:.3px}
  .company b{font-weight:600}
  .base-band{position:absolute;left:0;bottom:0;width:826px;height:14px;display:flex;gap:4px}
  .base-band i{display:block;height:100%;background:var(--gold)}
</style>
</head>
<body>
  <main class="flyer">
    <div class="hero-photo" role="img" aria-label="Dusk photograph of a house roof covered with solar panels, warm lit windows below"></div>
    <div class="hero-glow"></div>
    <div class="badge">ATTENTION<br>HOMEOWNER!</div>
    <div class="brand">SUNVALE BENEFITS <span class="brand-square"></span></div>

    <h1 class="headline">
      <div class="l1">BRIGHT</div>
      <div class="l2">HORIZON</div>
      <div class="l3">FORWARD</div>
    </h1>

    <p class="hook q">Are You FED UP With Your HIGH Electric Bills?</p>
    <p class="hook pay">WE WILL PAY YOU $2,000...</p>
    <p class="hook when">...When You Allow Us To</p>
    <span class="pill lower">PERMANENTLY LOWER YOUR</span>
    <p class="hook bill">ELECTRIC BILL By At Least</p>
    <span class="pill pct">25% To 50%!</span>

    <p class="intro">On Average, We Save homeowners <b>*33% OFF</b> Their Electricity Cost Every Month With Our New Cutting Edge Advanced Solar Technology, Without Taking 1 Penny From Your Current Monthly Budget. Government Subsidized!</p>

    <table class="rates">
      <tr><th>*IF YOUR Last 12 Months “Average Monthly Electric Payment” Is...</th></tr>
      <tr><td>*$100: Your NEW Monthly Fixed Payment Will Be $67 <small>($396 Annual Savings)</small></td></tr>
      <tr><td>*$200: Your NEW Monthly Fixed Payment Will Be $134 <small>($792 Annual Savings)</small></td></tr>
      <tr><td>*$300: Your NEW Monthly Fixed Payment Will Be $201 <small>($1,188 Annual Savings)</small></td></tr>
      <tr><td>*$400: Your NEW Monthly Fixed Payment Will Be $268 <small>($1,584 Annual Savings)</small></td></tr>
      <tr><td>*$500: Your NEW Monthly Fixed Payment Will Be $335 <small>($1,980 Annual Savings)</small></td></tr>
    </table>

    <p class="offer">IF YOU OWN YOUR HOME, WE WILL SEND YOU OUR <b>“NOBEL PRIZE WINNING TECHNOLOGY”</b> THAT WILL <b>ELIMINATE $200 OF YOUR GAS OR DIESEL FUEL EXPENSE</b> When You Allow Us To <b>Do A NO COST, NO OBLIGATION ENERGY SAVINGS ANALYSIS</b> And Share YOUR MONEY <b>SAVING RESULTS</b> With You Via A 30 Minute Video Meeting.</p>

    <div class="url">WWW.SUNVALEBENEFITS.ENERGY</div>
    <p class="cta">TO REQUEST YOUR COMPLIMENTARY ENERGY SAVINGS ANALYSIS &amp; TO <span>ACCEPT OUR $200 GIFT.</span></p>

    <div class="contact">
      <p class="phone">888-555-0142 EXT. 204</p>
      <p class="rep">MARA LINDEN</p>
    </div>
    <div class="divider"></div>
    <div class="company">
      <div class="name">VANTORA FIELD WORKS, LLC</div>
      <div><b>CORP OFFICE:</b> 4210 Desert Bloom Ave. Las Vegas, NV 89100</div>
      <div><b>REGIONAL OFFICE:</b> 615 Orchard Lane Fresno, CA 93700</div>
    </div>

    <div class="base-band"><i style="width:40px"></i><i style="width:280px"></i><i style="width:490px;background:var(--orange)"></i></div>
  </main>
</body>
</html>
```